Online Marketplace Startup for Community Facilities (Tovaroom)

A innovative, modern website design is required for a new startup called Tovaroom. Tovaroom will be an online marketplace for searching for and booking community facilities, such as schools facilities (sports grounds, halls, classrooms etc.), churches, hospitals and other community facilities.

The attached brief has been created to provide guidance on the structure and content required.

The web design shall feature a modern, innovative but user friendly interface similar style to other web start up pages:
www.hallquiver.co.uk
www.vendlark.com.au
www.artfennel.com.au

The web design shall be ‘wordpress’ compliant and allow for future functionality to be added and coded (e.g. animations, flash, blogs etc) and content to be editable.

The following brief has been created to provide guidance on the structure and content required.

An existing logo developed for Tovaroom shall be utilised and incorporated in the top left hand cover of the cover landing page (refer to attached logo designs).

Refer to attached 'Website brief' for more details on requirements.
Updates

Project Deadline Extended
Reason: I wish to grant an extension to the deadline to provide designers with more time to submit their designs.

Target Market(s)

TovaRoom will focus on building a customer network of both community facility owners (schools, hospitals, churches) and hirers (non-government organisations, community groups, event management companies, commercial businesses). Members of the general public will also be encouraged to book facilities for private functions.

Industry/Entity Type

Community

Coding

Coded - Design and coding required

Number of Pages Required

5+ page

Font styles to use
Sans Serif

Colors
3176b5
ffffff
85cae6
33a6d7

Requirements
Must have
• The web design shall feature a modern, innovative but user friendly interface similar style to other web start up pages:
• www.hallquiver.co.uk
• www.vendlark.com.au
• www.artfennel.com.au
• The web design shall be ‘wordpress’ compliant and allow for future functionality to be added and coded (e.g. animations, flash, blogs etc) and content to be editable.
• Refer to Project brief for other requirements
Nice to have
• Refer to Project brief
Should not have
• Refer to Project brief

```html
<!DOCTYPE html>
<html lang="en">
<head>
<meta charset="utf-8">
<title>TovaRoom — Community Facility Bookings</title>
<link href="https://fonts.googleapis.com/css2?family=Raleway:wght@400;500;600;800&family=Roboto:ital,wght@0,400;0,500;0,700;1,700&display=swap" rel="stylesheet">
<style>
:root{
  --brand:#3176b5;
  --brand-dark:#1f4f9c;
  --sky:#85cae6;
  --accent:#33a6d7;
  --bright:#08a4ea;
  --teal:#1fbfcf;
  --white:#ffffff;
  --ink:#333a40;
  --muted:#6b7178;
  --grey-band:#ececec;
  --field:#e0e0e0;
  --line:#9e9e9e;
}
*{box-sizing:border-box;margin:0;padding:0}
html,body{width:1200px;height:3557px;overflow:hidden}
body{font-family:'Roboto',sans-serif;color:var(--ink);background:var(--white);position:relative}
.abs{position:absolute}
h2{font-family:'Raleway',sans-serif;font-weight:400;color:var(--ink)}
.btn{display:flex;align-items:center;justify-content:center;background:var(--accent);color:var(--white);font-size:15px;font-family:'Roboto',sans-serif}

/* top bar */
.topbar{top:0;left:0;width:1200px;height:43px;background:var(--brand)}
.topbar .contact{top:0;height:43px;display:flex;align-items:center;gap:10px;color:#dfeaf6;font-size:13px}
.social{display:flex;gap:14px}
.social span{width:24px;height:24px;border-radius:50%;background:var(--white);display:block}
.topbar .social{top:9px;right:42px}

/* nav */
.nav{top:43px;left:0;width:1200px;height:76px;background:var(--white)}
.logo{display:flex;align-items:center;gap:10px;font-family:'Raleway',sans-serif;font-weight:600;color:var(--brand-dark)}
.nav .logo{left:28px;top:18px;font-size:38px}
.logo i{display:block;width:30px;height:30px;border-radius:50%;background:var(--brand-dark)}
.menu{right:38px;top:0;height:76px;display:flex;gap:36px;align-items:center;font-size:13px;color:#555}
.menu .active{color:var(--brand);position:relative}
.menu .active::after{content:"";position:absolute;left:0;right:0;bottom:-30px;height:3px;background:var(--brand)}

/* hero */
.hero{top:119px;left:0;width:1200px;height:524px;background:linear-gradient(180deg,#2c3a4c 0%,#4f6478 40%,#3d5060 62%,#7a5a3a 78%,#25323d 100%)}
.hero .lead{top:160px;width:1200px;text-align:center;font-family:'Raleway',sans-serif;font-size:34px;color:var(--white)}
.hero .title{top:204px;width:1200px;text-align:center;font-family:'Raleway',sans-serif;font-weight:800;font-size:44px;color:var(--white)}
.hero .btn{top:300px;width:130px;height:38px}
.btn-ghost{background:transparent !important;border:2px solid var(--white)}

/* services */
.services-title{left:57px;top:750px;font-size:34px}
.services-title b{font-weight:500}
.services-intro{left:57px;top:810px;width:480px;font-size:13px;font-weight:700;font-style:italic;line-height:27px;color:#444}
.services-text{left:57px;top:884px;width:480px;font-size:13px;line-height:27px;color:var(--muted)}
.services .read{left:57px;top:1030px;width:109px;height:37px;font-size:13px}
.tile{width:258px;height:142px;border:6px solid var(--white);outline:3px solid var(--brand);display:flex;flex-direction:column;align-items:center;justify-content:flex-end;padding-bottom:18px;gap:14px;color:var(--white);font-size:12px;text-align:center;line-height:17px;text-transform:uppercase}
.tile.light{background:var(--accent)}
.tile.dark{background:var(--brand)}

/* process */
.process{top:1205px;left:0;width:1200px;height:527px;background:var(--grey-band)}
.center{width:1200px;text-align:center}
.process h2{top:52px;font-size:32px}
.para{font-size:13px;line-height:25px;color:#555}
.process .para{top:122px;left:130px;width:940px}
.track{top:292px;left:80px;width:1040px;height:8px;background:var(--line)}
.track-done{top:292px;left:80px;width:250px;height:8px;background:var(--brand-dark)}
.step{width:60px;height:60px;border-radius:50%;background:var(--line);top:266px;display:flex;align-items:center;justify-content:center}
.step.done{background:var(--brand-dark)}
.caption{top:334px;width:240px;text-align:center;font-size:12.5px;line-height:24px;color:#444}
.process .btn{top:436px;left:536px;width:128px;height:36px;font-size:13px}

/* team */
.team-title{top:1836px;font-size:32px}
.team-para{top:1892px;left:190px;width:820px}
.member{top:2004px;width:240px;height:247px}
.tag{top:2251px;width:240px;height:67px;background:#f6f6f6;text-align:center;padding-top:14px}
.tag strong{display:block;font-size:11px;font-weight:700}
.tag em{display:block;font-size:10px;margin-top:8px;color:#666}
.tag.on{background:#222;color:var(--white)}
.tag.on em{color:#ccc}
.teal-band{top:2318px;left:0;width:1200px;height:21px;background:var(--teal)}

/* clients */
.clients-title{top:2427px;font-size:32px}
.client{top:2554px;width:180px;text-align:center;font-family:'Raleway',sans-serif;font-weight:600;font-size:34px;color:#444}

/* contact band */
.band{top:2723px;left:0;width:1200px;height:159px;background:var(--bright)}
.band .half{top:0;height:159px;width:600px}
.band .right{left:600px;background:#0c9de3}
.band small{position:absolute;top:40px;font-size:13px;line-height:17px;color:#bfe6fb}
.band strong{position:absolute;top:95px;font-size:28px;font-weight:500;color:var(--white)}
.or{top:2781px;left:578px;width:44px;height:44px;border-radius:50%;background:#1890cf;color:var(--white);font-size:13px;display:flex;align-items:center;justify-content:center}

/* enquiry */
.enq-title{top:2958px;font-size:34px}
.enq-sub{top:3008px;font-size:18px;color:#444;font-family:'Raleway',sans-serif}
.field{left:19px;width:567px;height:48px;background:var(--field);border-radius:4px;font-size:12px;color:#555;padding:14px 18px}
.message{left:607px;top:3062px;width:572px;height:244px;background:var(--field);border-radius:4px;font-size:12px;color:#555;padding:16px 20px}
.submit{top:3359px;left:515px;width:170px;height:35px;font-size:13px}

/* footer */
.footer-line{top:3444px;left:19px;width:1160px;height:2px;background:#ccc}
.footer-logo{left:28px;top:3462px;font-size:34px}
.copy{left:19px;top:3515px;font-size:12px;color:#666}
.footer-social{right:40px;top:3473px}
.footer-social span{background:#eee}
</style>
</head>
<body>

<header class="abs topbar">
  <div class="abs contact" style="left:30px">
    <svg width="12" height="18" viewBox="0 0 12 18"><rect x="1" y="1" width="10" height="16" rx="2" fill="none" stroke="#fff" stroke-width="1.6"/><circle cx="6" cy="14" r="1" fill="#fff"/></svg>
    (041) 552 180 736
  </div>
  <div class="abs contact" style="left:228px">
    <svg width="18" height="13" viewBox="0 0 18 13"><rect x="1" y="1" width="16" height="11" fill="none" stroke="#fff" stroke-width="1.4"/><path d="M1 1l8 6 8-6" fill="none" stroke="#fff" stroke-width="1.4"/></svg>
    hello@tovaroom.com
  </div>
  <div class="abs social"><span></span><span></span><span></span><span></span></div>
</header>

<nav class="abs nav">
  <div class="abs logo"><i></i>TovaRoom</div>
  <div class="abs menu">
    <span class="active">HOME</span><span>ABOUT US</span><span>HOW IT WORKS</span><span>SERVICES</span><span>WHY USE US</span><span>FAQ</span><span>CONTACT US</span>
  </div>
</nav>

<section class="abs hero" role="img" aria-label="Resort pool area with palm trees at dusk">
  <p class="abs lead">Utilising your facility to create value for your</p>
  <h1 class="abs title">ORGANISATION AND THE COMMUNITY</h1>
  <div class="abs btn btn-ghost" style="left:446px">Know More</div>
  <div class="abs btn" style="left:598px">Get Started</div>
</section>

<section class="services">
  <h2 class="abs services-title">Our <b>Services</b></h2>
  <p class="abs services-intro">We provide a cloud based online solution for managing your facility lettings, marketing and promotion of your facility and on-site supervision services.</p>
  <p class="abs services-text">Lorem Ipsum is simply dummy text of the printing and typesetting industry. Lorem Ipsum has been the industry's standard dummy text ever since the 1500s, when an unknown printer took a galley of type and scrambled it to make a type specimen book.</p>
  <div class="abs btn read">Read More</div>

  <div class="abs tile light" style="left:636px;top:738px">
    <svg width="60" height="48" viewBox="0 0 60 48" fill="none" stroke="#fff" stroke-width="2"><circle cx="30" cy="24" r="8"/><rect x="6" y="4" width="12" height="14"/><rect x="42" y="4" width="12" height="14"/><rect x="6" y="30" width="12" height="14"/><rect x="42" y="30" width="12" height="14"/></svg>
    <span>Marketing &amp; Promotion<br>of your facility</span>
  </div>
  <div class="abs tile dark" style="left:904px;top:738px">
    <svg width="60" height="48" viewBox="0 0 60 48" fill="none" stroke="#fff" stroke-width="2"><rect x="6" y="4" width="48" height="32"/><path d="M20 44h20M30 36v8"/><circle cx="30" cy="18" r="6"/></svg>
    <span>Administer bookings<br>and enquiries</span>
  </div>
  <div class="abs tile dark" style="left:636px;top:890px">
    <svg width="60" height="48" viewBox="0 0 60 48" fill="none" stroke="#fff" stroke-width="2"><rect x="14" y="2" width="26" height="36"/><rect x="22" y="10" width="26" height="36"/><path d="M28 20h14M28 28h14M28 36h10"/></svg>
    <span>Invoices and payment<br>collection</span>
  </div>
  <div class="abs tile light" style="left:904px;top:890px">
    <svg width="60" height="48" viewBox="0 0 60 48" fill="none" stroke="#fff" stroke-width="2"><circle cx="30" cy="18" r="11"/><path d="M12 46c2-10 10-15 18-15s16 5 18 15"/><path d="M17 18h-4v8h4M43 18h4v8h-4"/></svg>
    <span>Bookings reports<br>and customer service</span>
  </div>
</section>

<section class="abs process">
  <h2 class="abs center" style="top:52px;font-size:32px">How Does Booking &nbsp;Process Work?</h2>
  <p class="abs para center" style="left:130px;width:940px;top:122px">Lorem Ipsum is simply dummy text of the printing and typesetting industry. Lorem Ipsum has been the industry's standard dummy text ever since the 1500s, when an unknown printer took a galley of type and scrambled it to make a type specimen book.</p>
  <div class="abs track"></div>
  <div class="abs track-done"></div>
  <div class="abs step done" style="left:174px"><svg width="28" height="28" viewBox="0 0 28 28" fill="none" stroke="#fff" stroke-width="2"><circle cx="12" cy="12" r="7"/><path d="M17 17l7 7"/></svg></div>
  <div class="abs step" style="left:430px"><svg width="26" height="26" viewBox="0 0 26 26" fill="none" stroke="#fff" stroke-width="2"><rect x="3" y="3" width="20" height="20"/><path d="M8 13l4 4 7-8"/></svg></div>
  <div class="abs step" style="left:701px"><svg width="26" height="26" viewBox="0 0 26 26" fill="none" stroke="#fff" stroke-width="2"><rect x="3" y="5" width="20" height="18"/><path d="M3 10h20M8 2v5M18 2v5"/></svg></div>
  <div class="abs step" style="left:966px"><svg width="26" height="26" viewBox="0 0 26 26" fill="none" stroke="#fff" stroke-width="2"><rect x="5" y="3" width="16" height="20"/><path d="M9 9h8M9 13h8M9 17h5"/></svg></div>
  <p class="abs caption" style="left:84px">Client/hirer looks for advertised space / facility via TovaRoom online platform and makes application</p>
  <p class="abs caption" style="left:340px">Application evaluated by TovaRoom based on guidelines &amp; criteria agreed with facility (history insurances)</p>
  <p class="abs caption" style="left:611px">Booking of facility made via TovaRoom online bookings platform</p>
  <p class="abs caption" style="left:876px">Invoice generated and payment received prior to hire of facility</p>
  <div class="abs btn" style="top:436px;left:536px;width:128px;height:36px;font-size:13px">BOOK NOW</div>
</section>

<section class="team">
  <h2 class="abs center team-title">Meet Our Team</h2>
  <p class="abs para center team-para">Lorem Ipsum is simply dummy text of the printing and typesetting industry. Lorem Ipsum has been the industry's standard dummy text ever since the 1500s, when an unknown printer took a galley of type and scrambled it to make a type specimen book.</p>
  <div class="abs member" style="left:0;background:linear-gradient(180deg,#d9d9d9,#8a8f6a)" role="img" aria-label="Portrait of team member, principal"></div>
  <div class="abs member" style="left:240px;background:linear-gradient(180deg,#e4e4e4,#b8333c)" role="img" aria-label="Portrait of team member, school nurse"></div>
  <div class="abs member" style="left:480px;background:linear-gradient(180deg,#e6e6e6,#c9a430)" role="img" aria-label="Portrait of team member, career counsellor"></div>
  <div class="abs member" style="left:720px;background:linear-gradient(180deg,#a8a8a8,#4e4e4e)" role="img" aria-label="Portrait of team member, teacher"></div>
  <div class="abs member" style="left:960px;background:linear-gradient(180deg,#e8e8e8,#6ec7c6)" role="img" aria-label="Portrait of team member, assistant teacher"></div>
  <div class="abs social" style="left:797px;top:2200px;gap:8px"><span></span><span></span><span></span></div>
  <div class="abs tag" style="left:0"><strong>PERRY LINDQVIST</strong><em>Principal</em></div>
  <div class="abs tag" style="left:240px;background:#ececec"><strong>NADIA FARROW</strong><em>School Nurse</em></div>
  <div class="abs tag" style="left:480px"><strong>GRETA MUNROE</strong><em>Career Counsellor</em></div>
  <div class="abs tag on" style="left:720px"><strong>ELIAS OKAFOR</strong><em>Teacher</em></div>
  <div class="abs tag" style="left:960px"><strong>TESSA QUINLAN</strong><em>Assistant Teacher</em></div>
  <div class="abs teal-band"></div>
</section>

<section class="clients">
  <h2 class="abs center clients-title">Our Valuable Clients</h2>
  <svg class="abs" style="left:34px;top:2563px" width="16" height="26" viewBox="0 0 16 26"><path d="M13 2L3 13l10 11" fill="none" stroke="#333" stroke-width="3"/></svg>
  <svg class="abs" style="left:1144px;top:2563px" width="16" height="26" viewBox="0 0 16 26"><path d="M3 2l10 11L3 24" fill="none" stroke="#333" stroke-width="3"/></svg>
  <p class="abs client" style="left:70px">KORVEL&amp;CO</p>
  <p class="abs client" style="left:275px">TANDOX</p>
  <p class="abs client" style="left:480px">EXVANTA</p>
  <p class="abs client" style="left:690px">STURDEN</p>
  <p class="abs client" style="left:900px">LAHAVEN</p>
</section>

<section class="abs band">
  <div class="abs half">
    <svg class="abs" style="left:100px;top:40px" width="22" height="36" viewBox="0 0 22 36"><rect x="2" y="2" width="18" height="32" rx="3" fill="none" stroke="#fff" stroke-width="2.4"/><circle cx="11" cy="28" r="1.8" fill="#fff"/></svg>
    <small style="left:150px">Call now<br>for free consultation</small>
    <strong style="left:100px">: &nbsp;&nbsp;(041) 552 180 900</strong>
  </div>
  <div class="abs half right">
    <svg class="abs" style="left:64px;top:42px" width="36" height="30" viewBox="0 0 36 30"><path d="M2 12L18 2l16 10v16H2z M2 12l16 10 16-10" fill="none" stroke="#fff" stroke-width="2.4"/></svg>
    <small style="left:116px">Mail now<br>free consultation</small>
    <strong style="left:64px">: &nbsp;&nbsp;hello@tovaroom.com</strong>
  </div>
</section>
<div class="abs or">OR</div>

<section class="enquiry">
  <h2 class="abs center enq-title">Enquiry Form</h2>
  <p class="abs center enq-sub">Enquire now or request a demo</p>
  <div class="abs field" style="top:3062px">Your Name</div>
  <div class="abs field" style="top:3124px">Address</div>
  <div class="abs field" style="top:3186px">Phone</div>
  <div class="abs field" style="top:3249px">Email</div>
  <div class="abs message">Your Message</div>
  <div class="abs btn submit">SUBMIT</div>
</section>

<footer>
  <div class="abs footer-line"></div>
  <div class="abs logo footer-logo"><i></i>TovaRoom</div>
  <p class="abs copy">© 2017 Tovaroom Pty. Ltd.</p>
  <div class="abs social footer-social"><span></span><span></span><span></span><span></span></div>
</footer>

</body>
</html>
```